Loftvane.ca Your Canadian Source for all your mortgage needs.

I need to get a fresh look on my current website. It is not currently a Wordpress site and i need to build a whole new site that i can do my editing in using Wordpress.
I need it built in a mobile or responsive theme.
There will be a secured application page which is critical.
I have 3 books written so i want to be able to have advertising spaces for promoting them and a landing page ( I can build my own landing pages)
I need the frame work of a professional theme with easy editing capabilities.
I have my own LOGOs which i would continue to use. The current site can be reviewed at www.loftvane.ca.
The front page could have a young couple near a nice house, open to suggestions.
I don't need a blog post to update but if it was on the sides of the pages I could use it. Something like a "Latest News" section.
I would like to have a Main page, Application Page, Resource page, Contact page, Calculator Page, a questions and answer page. Theses can be populated with the current information or I can add latter.
I want the main page to be a mini sales page so I can link to Posts on First Time Home Buyers, Refinance Options, Second Home or New purchase options.
I provide mortgages for people across Canada so i want the Canadian Flag incorporated
I like the colors to work with the logo colors on the current site

Target Market(s)

Canadian Mortgage Clients

Font styles to use
Sans Serif

Colors
3277b5
cadf82

Requirements
Must have
• Must work in a Wordpress Theme
• Please see Project description for more details
Nice to have
• Space to add banner ads for my books. I have 3 books written

```html
<!DOCTYPE html>
<html lang="en">
<head>
<meta charset="utf-8">
<title>Loftvane.ca – Your Canadian Source for All Your Mortgage Needs</title>
<link rel="stylesheet" href="https://fonts.googleapis.com/css2?family=Open+Sans:wght@400;600;700;800&display=swap">
<style>
:root{
  --blue:#3277b5;
  --blue-dark:#1f5a93;
  --navy:#1b4a7d;
  --navy-deep:#143a63;
  --green:#cadf82;
  --green-dark:#8fb23a;
  --flag-tone:#e4a39d;
  --page:#eef1f4;
  --card:#ffffff;
  --text:#4a4f55;
  --muted:#7b8289;
  --line:#d6dce2;
}
*{box-sizing:border-box;margin:0;padding:0}
html,body{width:1200px;height:2272px;overflow:hidden}
body{font-family:"Open Sans",Arial,sans-serif;color:var(--text);background:var(--page);font-size:15px;line-height:1.5}
a{color:inherit;text-decoration:none}

/* header */
.site-header{height:112px;background:#fff;display:flex;align-items:center;justify-content:space-between;padding:0 60px}
.brand{display:flex;align-items:center;gap:12px}
.brand-mark{width:34px;height:34px;background:var(--blue);border-radius:50%}
.brand-name{font-size:34px;font-weight:800;color:var(--blue);letter-spacing:.5px}
.header-right{display:flex;align-items:center;gap:26px}
.flags{width:104px;height:52px;background:linear-gradient(135deg,#f3d6d3,var(--flag-tone));border-radius:2px}
.header-contact{display:flex;flex-direction:column;align-items:flex-end;gap:8px}
.call{display:flex;align-items:center;gap:10px}
.call-icon{width:34px;height:34px;border-radius:50%;background:var(--blue);display:flex;align-items:center;justify-content:center}
.call-text{line-height:1.1}
.call-text small{display:block;font-size:11px;color:var(--muted);font-weight:600}
.call-text strong{font-size:22px;color:var(--blue-dark);font-weight:800}
.socials{display:flex;gap:6px}
.social{width:24px;height:24px;border-radius:50%;background:var(--blue)}

/* nav */
.main-nav{height:32px;background:var(--blue);display:flex;align-items:center;padding:0 60px;gap:4px}
.main-nav a{color:#fff;font-size:13px;font-weight:700;text-transform:uppercase;padding:0 18px;height:32px;display:flex;align-items:center}
.main-nav a.active{background:var(--blue-dark)}

/* hero */
.hero{position:relative;height:428px;overflow:hidden}
.hero-photo{position:absolute;inset:0;background:linear-gradient(100deg,#c9dbea 0%,#9cbcd6 30%,#c7d4b9 55%,#8aa86a 80%,#5d7f45 100%)}
.hero-copy{position:absolute;right:70px;top:80px;width:470px;color:#fff}
.hero-copy h1{font-size:40px;font-weight:800;line-height:1.05;text-transform:uppercase;text-shadow:0 2px 6px rgba(0,0,0,.35)}
.hero-copy p{margin-top:12px;font-size:17px;font-weight:700;text-transform:uppercase;line-height:1.3;background:rgba(20,58,99,.75);padding:10px 14px}
.hero-arrow{position:absolute;top:188px;width:30px;height:46px;background:rgba(20,58,99,.7);display:flex;align-items:center;justify-content:center}
.hero-arrow.prev{left:0}.hero-arrow.next{right:0}

/* features */
.features{position:relative;margin-top:-30px;display:flex;gap:40px;padding:0 74px;z-index:2}
.feature{flex:1;background:var(--card);text-align:center;box-shadow:0 2px 6px rgba(0,0,0,.12);padding-top:54px;position:relative;height:280px}
.feature-icon{position:absolute;top:-40px;left:50%;transform:translateX(-50%);width:80px;height:80px;border-radius:50%;background:var(--blue);border:5px solid #fff;box-shadow:0 1px 4px rgba(0,0,0,.2);display:flex;align-items:center;justify-content:center}
.feature h2{font-size:16px;font-weight:800;color:var(--navy);text-transform:uppercase;line-height:1.2;padding:0 20px}
.feature-body{position:absolute;left:0;right:0;bottom:0;height:170px;background:var(--green);padding:20px 26px 0}
.feature-body p{font-size:13px;color:#4a5a2a;line-height:1.45}
.btn-small{display:inline-block;margin-top:22px;background:#fff;color:var(--navy);font-size:12px;font-weight:700;padding:6px 16px;border:1px solid #b3c86a}

/* intro + news */
.intro-row{display:flex;gap:30px;padding:0 74px;margin-top:40px;height:440px}
.why{flex:1}
.section-title{font-size:26px;font-weight:800;color:var(--blue);text-transform:uppercase}
.why p{font-size:14px;margin-top:14px;line-height:1.6}
.btn{display:inline-block;margin-top:18px;background:var(--green);color:var(--navy);font-size:13px;font-weight:700;padding:8px 20px}
.news{width:330px;background:#e3e8ed;align-self:flex-start}
.news-head{background:var(--blue);color:#fff;font-size:18px;font-weight:800;text-transform:uppercase;padding:10px 18px}
.news-item{padding:10px 18px;border-bottom:1px solid var(--line);font-size:12.5px}
.news-item time{display:block;font-size:11px;color:var(--muted)}

/* books */
.books{display:flex;gap:40px;padding:0 74px;height:250px}
.book{flex:1;background:linear-gradient(#cde0f0,#a9c7e2);display:flex;align-items:center;justify-content:center}
.book-cover{width:190px;height:210px;background:linear-gradient(135deg,#6a9c3a,#c9a23a 55%,#3c6e9c)}

/* newsletter */
.newsletter{margin:50px 74px 0;background:#fff;height:190px;text-align:center;padding-top:26px}
.newsletter h2{font-size:24px;font-weight:800;color:var(--blue)}
.newsletter h3{font-size:14px;font-weight:700;color:var(--navy);margin-top:14px}
.signup{display:flex;justify-content:center;margin-top:14px}
.signup input{width:560px;height:44px;border:1px solid var(--line);padding:0 14px;font-family:inherit;font-size:13px;color:var(--muted)}
.signup button{height:44px;background:var(--blue);color:#fff;border:0;font-family:inherit;font-weight:700;font-size:13px;padding:0 22px;text-transform:uppercase}

/* footer */
.site-footer{position:absolute;left:0;right:0;top:1872px;height:400px;background:var(--navy)}
.contact-strip{height:80px;background:var(--blue-dark);display:flex;align-items:center;padding:0 74px;gap:50px}
.strip-title{font-size:22px;font-weight:800;color:var(--green);line-height:1.05;text-transform:uppercase;width:170px}
.strip-item{display:flex;align-items:center;gap:10px;color:#fff;font-size:12px;line-height:1.2;font-weight:600}
.strip-item strong{display:block;font-size:14px;font-weight:800;text-transform:uppercase}
.strip-icon{width:36px;height:36px;border-radius:50%;background:var(--green);display:flex;align-items:center;justify-content:center}
.footer-cols{display:flex;padding:26px 74px 0;gap:40px;height:260px;color:#c9d6e4;font-size:12.5px}
.footer-col{flex:1}
.footer-col h4{color:#fff;font-size:14px;font-weight:800;margin-bottom:10px}
.footer-col ul{list-style:none}
.footer-col li{line-height:1.75}
.event{margin-bottom:10px}
.event time{color:var(--green);font-size:11.5px;display:block}
.footer-socials{display:flex;gap:8px}
.footer-socials span{width:32px;height:32px;border-radius:50%;background:var(--blue)}
.copyright{height:60px;background:var(--navy-deep);color:#9fb3c8;font-size:12px;display:flex;align-items:center;justify-content:center}
</style>
</head>
<body>

<header class="site-header">
  <a class="brand" href="#"><span class="brand-mark"></span><span class="brand-name">Loftvane</span></a>
  <div class="header-right">
    <div class="flags" role="img" aria-label="Two crossed Canadian flags on poles"></div>
    <div class="header-contact">
      <div class="call">
        <span class="call-icon"><svg width="16" height="16" viewBox="0 0 24 24"><path fill="#fff" d="M6.6 10.8a15 15 0 0 0 6.6 6.6l2.2-2.2a1 1 0 0 1 1-.25 11.4 11.4 0 0 0 3.6.57 1 1 0 0 1 1 1V20a1 1 0 0 1-1 1A17 17 0 0 1 3 4a1 1 0 0 1 1-1h3.5a1 1 0 0 1 1 1c0 1.25.2 2.45.57 3.57a1 1 0 0 1-.25 1z"/></svg></span>
        <span class="call-text"><small>CALL US</small><strong>403-555-0148</strong></span>
      </div>
      <div class="socials"><span class="social"></span><span class="social"></span><span class="social"></span></div>
    </div>
  </div>
</header>

<nav class="main-nav">
  <a class="active" href="#">Home</a><a href="#">Application</a><a href="#">Resource</a><a href="#">Calculator</a><a href="#">FAQs</a><a href="#">Contact Us</a>
</nav>

<section class="hero">
  <div class="hero-photo" role="img" aria-label="Young couple smiling in front of a new family home with a green lawn"></div>
  <div class="hero-copy">
    <h1>Customize Your Mortgage</h1>
    <p>And learn how to save thousands of dollars on your current or next mortgage</p>
  </div>
  <a class="hero-arrow prev" href="#"><svg width="12" height="18" viewBox="0 0 12 18"><path d="M10 2 3 9l7 7" fill="none" stroke="#fff" stroke-width="3"/></svg></a>
  <a class="hero-arrow next" href="#"><svg width="12" height="18" viewBox="0 0 12 18"><path d="m2 2 7 7-7 7" fill="none" stroke="#fff" stroke-width="3"/></svg></a>
</section>

<section class="features">
  <article class="feature">
    <span class="feature-icon"><svg width="34" height="34" viewBox="0 0 24 24"><circle cx="12" cy="8" r="4" fill="#fff"/><path d="M4 21c0-4.4 3.6-7 8-7s8 2.6 8 7z" fill="#fff"/></svg></span>
    <h2>Apply Online Now!</h2>
    <div class="feature-body">
      <p>Get fast pre-approval from the lenders. Apply in 15 min and work with a trusted broker.</p>
      <a class="btn-small" href="#">Click Here »</a>
    </div>
  </article>
  <article class="feature">
    <span class="feature-icon"><svg width="34" height="34" viewBox="0 0 24 24"><rect x="5" y="3" width="14" height="18" rx="1" fill="#fff"/><path d="M8 8h8M8 12h8M8 16h5" stroke="#3277b5" stroke-width="1.6"/></svg></span>
    <h2>Save Thousands<br>on Your Mortgage</h2>
    <div class="feature-body">
      <p>Customize your own mortgage and save thousands on your next home.</p>
      <a class="btn-small" href="#">Free PDF Document »</a>
    </div>
  </article>
  <article class="feature">
    <span class="feature-icon"><svg width="34" height="34" viewBox="0 0 24 24"><rect x="5" y="2" width="14" height="20" rx="2" fill="#fff"/><rect x="7.5" y="4.5" width="9" height="4" fill="#3277b5"/><g fill="#3277b5"><rect x="7.5" y="11" width="2.5" height="2.5"/><rect x="10.75" y="11" width="2.5" height="2.5"/><rect x="14" y="11" width="2.5" height="2.5"/><rect x="7.5" y="15" width="2.5" height="2.5"/><rect x="10.75" y="15" width="2.5" height="2.5"/><rect x="14" y="15" width="2.5" height="2.5"/></g></svg></span>
    <h2>Mortgage<br>Calculators</h2>
    <div class="feature-body">
      <p>Quickly compare payments, rates and terms with our easy tools.</p>
      <a class="btn-small" href="#">Click Here »</a>
    </div>
  </article>
</section>

<section class="intro-row">
  <div class="why">
    <h2 class="section-title">Why Use a Mortgage Broker?</h2>
    <p>Professional representation for you and your family to help negotiate one of your biggest investments in your life. Helping you plan your mortgage to save you the most money.</p>
    <p>A personalized "Mortgage Action Plan" which helps you to plan your mortgage that best suits you and your family's needs. Teaching you how to save thousands on your mortgage and allowing you to review and compare options both today and into the future.</p>
    <p>Personal Service to your convenience "Where you want it when you want it".</p>
    <p>We will help you save thousands with rate discounts and other mortgage tips. At the same time keeping you informed of new products or developments that could benefit you and your family.</p>
    <a class="btn" href="#">Read more »</a>
  </div>
  <aside class="news">
    <div class="news-head">Latest News</div>
    <div class="news-item"><time>16 Aug 2015</time>Lorem ipsum dolor sit amet, consectetur adipiscing elit.</div>
    <div class="news-item"><time>16 Aug 2015</time>Lorem ipsum dolor sit amet, consectetur adipiscing elit.</div>
    <div class="news-item"><time>16 Aug 2015</time>Lorem ipsum dolor sit amet, consectetur adipiscing elit.</div>
    <div class="news-item"><time>16 Aug 2015</time>Lorem ipsum dolor sit amet, consectetur adipiscing elit.</div>
    <div class="news-item"><time>16 Aug 2015</time>Lorem ipsum dolor sit amet, consectetur adipiscing elit.</div>
  </aside>
</section>

<section class="books">
  <div class="book"><div class="book-cover" role="img" aria-label="Book cover: Canadian first time home buyers guide"></div></div>
  <div class="book"><div class="book-cover" role="img" aria-label="Book cover: mortgage secrets revealed"></div></div>
  <div class="book"><div class="book-cover" role="img" aria-label="Book cover: how to save thousands on your mortgage"></div></div>
</section>

<section class="newsletter">
  <h2>Get Our Newsletters</h2>
  <h3>Want To Be On Our Mailing List? Get Our Newsletter</h3>
  <form class="signup"><input type="text" value="Enter your mail address" aria-label="Email address"><button type="button">Subscribe Now</button></form>
</section>

<footer class="site-footer">
  <div class="contact-strip">
    <div class="strip-title">Have<br>Questions?</div>
    <div class="strip-item"><span class="strip-icon"><svg width="16" height="16" viewBox="0 0 24 24"><path fill="#1b4a7d" d="M6.6 10.8a15 15 0 0 0 6.6 6.6l2.2-2.2a1 1 0 0 1 1-.25 11.4 11.4 0 0 0 3.6.57 1 1 0 0 1 1 1V20a1 1 0 0 1-1 1A17 17 0 0 1 3 4a1 1 0 0 1 1-1h3.5a1 1 0 0 1 1 1c0 1.25.2 2.45.57 3.57a1 1 0 0 1-.25 1z"/></svg></span><span>Call us<strong>403-555-0148</strong></span></div>
    <div class="strip-item"><span class="strip-icon"><svg width="18" height="14" viewBox="0 0 18 14"><rect x="1" y="1" width="16" height="12" fill="none" stroke="#1b4a7d" stroke-width="2"/><path d="m1 1 8 7 8-7" fill="none" stroke="#1b4a7d" stroke-width="2"/></svg></span><span>Send us<strong>an Email</strong></span></div>
    <div class="strip-item"><span class="strip-icon"><svg width="14" height="18" viewBox="0 0 14 18"><path d="M7 0a7 7 0 0 0-7 7c0 5 7 11 7 11s7-6 7-11a7 7 0 0 0-7-7z" fill="#1b4a7d"/><circle cx="7" cy="7" r="2.5" fill="#cadf82"/></svg></span><span>Find a<strong>Local Office</strong></span></div>
    <div class="strip-item"><span class="strip-icon"><svg width="16" height="16" viewBox="0 0 16 16"><path d="m2 8 4 4 8-9" fill="none" stroke="#1b4a7d" stroke-width="2.4"/></svg></span><span>Read the<strong>FAQs</strong></span></div>
  </div>
  <div class="footer-cols">
    <div class="footer-col">
      <h4>Contact Us</h4>
      <p>Loftvane Mortgages Inc.<br>Suite 210, 48 Ridgeview Road NW<br>Calgary, Alberta T2X 0A1</p>
    </div>
    <div class="footer-col">
      <h4>Upcoming Event</h4>
      <div class="event"><time>January 28 2015 - 7:00pm</time>Lorem ipsum dolor sit amet, con sectetur adipiscing elit.</div>
      <div class="event"><time>January 28 2015 - 7:00pm</time>Lorem ipsum dolor sit amet, con sectetur adipiscing elit.</div>
    </div>
    <div class="footer-col">
      <h4>Quick Links</h4>
      <ul><li>Home</li><li>Application</li><li>Resource</li><li>Calculator</li><li>FAQ's</li><li>Contact Us</li></ul>
    </div>
    <div class="footer-col">
      <h4>Connect with us</h4>
      <div class="footer-socials"><span></span><span></span><span></span></div>
    </div>
  </div>
  <div class="copyright">© 2015 Loftvane Mortgage. All Rights Reserved. &nbsp;•&nbsp; Terms and Conditions &nbsp;•&nbsp; Privacy Policy &nbsp;•&nbsp; Terms of Use</div>
</footer>

</body>
</html>
```